Looking for a Lumora Book Cover

My book has been online for a while and I am now looking for a professional cover for it as it has been very well received.

You can view the book here and all the details about it:

https://www.pagevaultshop.example/dp/X7Q2KRMTPL#readerNotes

Not sure what I am looking for as a design, just open to your ideas.

I want something different that will stand out please.

Thanks
Owen

```html
<!DOCTYPE html>
<html lang="en">
<head>
<meta charset="utf-8">
<title>Roots and Resilence — Book Cover</title>
<link rel="stylesheet" href="https://fonts.googleapis.com/css2?family=Montserrat:wght@600;700;800&display=swap">
<style>
  :root {
    --stage: #e9e6e1;
    --cover: #000000;
    --olive: #b8b83a;
    --orange: #d97a2c;
    --white: #ffffff;
    --portrait-light: #6a6a6a;
    --portrait-dark: #0a0a0a;
  }
  * { margin: 0; padding: 0; box-sizing: border-box; }
  html, body {
    width: 1200px; height: 1000px; overflow: hidden;
    background: var(--stage);
    font-family: "Montserrat", Arial, sans-serif;
  }
  .book-cover {
    position: absolute; left: 280px; top: 25px;
    width: 640px; height: 950px;
    background: var(--cover);
    box-shadow: 0 10px 30px rgba(0,0,0,0.25);
  }
  .title {
    position: absolute; top: 30px; left: 0; width: 100%;
    text-align: center; font-weight: 800; line-height: 0.95;
  }
  .title-roots { color: var(--olive); font-size: 78px; letter-spacing: 1px; }
  .title-and { color: var(--white); font-size: 44px; }
  .title-resilence { display: block; color: var(--orange); font-size: 82px; letter-spacing: 1px; }
  .subtitle {
    position: absolute; top: 228px; left: 0; width: 100%;
    text-align: center; color: var(--white);
    font-weight: 700; font-size: 22px; line-height: 1.6; letter-spacing: 1.5px;
  }
  .portrait {
    position: absolute; top: 340px; left: 80px;
    width: 480px; height: 400px;
    background: radial-gradient(ellipse at 55% 45%, var(--portrait-light) 0%, #2c2c2c 45%, var(--portrait-dark) 75%, var(--cover) 100%);
  }
  .tagline {
    position: absolute; top: 760px; left: 0; width: 100%;
    text-align: center; color: var(--white);
    font-weight: 700; font-size: 19px; line-height: 1.75; letter-spacing: 3.5px;
  }
  .tagline .accent { color: var(--olive); }
  .author-band {
    position: absolute; left: 0; bottom: 0; width: 100%; height: 46px;
    background: var(--orange);
    display: flex; align-items: center; justify-content: center;
    color: var(--white); font-weight: 700; font-size: 15px; letter-spacing: 4px;
  }
</style>
</head>
<body>
  <main class="book-cover">
    <h1 class="title">
      <span class="title-roots">ROOTS</span> <span class="title-and">AND</span>
      <span class="title-resilence">RESILENCE</span>
    </h1>
    <p class="subtitle">A CELEBRATION OF CULTURE, STRUGGLE<br>AND ACHIEVEMENT</p>
    <div class="portrait" role="img" aria-label="Black and white portrait of a person in profile, face turned upward, an orange butterfly resting on the nose, hair blending into roots below"></div>
    <p class="tagline">THE HISTORY, RESISTANCE<br><span class="accent">AND EXCELLENCE OF BLACK PEOPLE</span><br>IN AFRICA AND THE DIASPORA</p>
    <div class="author-band">ELIAS BRANWELL</div>
  </main>
</body>
</html>
```